Strong, modern, clean Business Card design

Looking for a stunning, but CLEAN business card design. While we are a faith-based organization, we do NOT want this to look religious.

Industry/Entity Type

Non-Profit

Contact Information for Business Card

Dale Munroe | Lead Pastor
dale@BrightHarvestHope.org
970-555-0148
PO Box 7316
Brookridge, ST 80571

Font styles to use
Serif
Sans Serif

Requirements
Should not have
• Religious imagery or symbolism

```html
<!DOCTYPE html>
<html lang="en">
<head>
<meta charset="utf-8">
<title>Harvest Hope Church – Business Card</title>
<link href="https://fonts.googleapis.com/css2?family=Roboto:wght@400;500&display=swap" rel="stylesheet">
<style>
  :root {
    --page-bg: #1c1c1c;
    --card-bg: #ffffff;
    --brand-blue: #4b7f9c;
    --text-grey: #555a5e;
    --rule-grey: #9a9a9a;
  }
  * { margin: 0; padding: 0; box-sizing: border-box; }
  html, body {
    width: 1200px;
    height: 960px;
    overflow: hidden;
    background: var(--page-bg);
  }
  .stage {
    width: 1200px;
    height: 960px;
    display: flex;
    align-items: center;
    justify-content: center;
  }
  .business-card {
    position: relative;
    width: 900px;
    height: 514px;
    background: var(--card-bg);
    box-shadow: 0 18px 40px rgba(0,0,0,0.55);
    font-family: "Roboto", Arial, sans-serif;
  }
  .brand-block {
    position: absolute;
    left: 40px;
    top: 0;
    width: 400px;
    height: 100%;
    display: flex;
    flex-direction: column;
    align-items: center;
    justify-content: center;
    padding-top: 60px;
  }
  .brand-name {
    color: var(--brand-blue);
    font-weight: 500;
    font-size: 38px;
    letter-spacing: 0.12em;
    text-transform: uppercase;
    line-height: 1.15;
    text-align: center;
  }
  .divider {
    position: absolute;
    left: 480px;
    top: 110px;
    width: 1.5px;
    height: 290px;
    background: var(--rule-grey);
  }
  .contact-block {
    position: absolute;
    left: 530px;
    top: 118px;
    color: var(--text-grey);
    font-size: 20px;
    line-height: 1.3;
  }
  .person-name {
    color: var(--brand-blue);
    font-weight: 500;
    font-size: 26px;
    letter-spacing: 0.01em;
    text-transform: uppercase;
  }
  .person-title { margin-bottom: 30px; padding-left: 16px; }
  .address { margin-bottom: 30px; padding-left: 40px; font-style: normal; }
  .contact-list { list-style: none; padding-left: 40px; }
  .contact-list li {
    display: flex;
    align-items: center;
    gap: 10px;
  }
  .contact-list svg { width: 17px; height: 17px; flex: none; }
</style>
</head>
<body>
<main class="stage">
  <section class="business-card">
    <div class="brand-block">
      <p class="brand-name">Harvest Hope<br>Church</p>
    </div>

    <div class="divider"></div>

    <div class="contact-block">
      <h1 class="person-name">Dale Munroe</h1>
      <p class="person-title">Lead Pastor</p>

      <address class="address">
        PO Box 7316<br>
        Brookridge, ST 80571
      </address>

      <ul class="contact-list">
        <li>
          <svg viewBox="0 0 24 24" aria-hidden="true"><path fill="#4b7f9c" d="M6.6 10.8c1.4 2.8 3.8 5.1 6.6 6.6l2.2-2.2c.3-.3.7-.4 1-.2 1.1.4 2.3.6 3.6.6.6 0 1 .4 1 1V20c0 .6-.4 1-1 1C10.6 21 3 13.4 3 4c0-.6.4-1 1-1h3.5c.6 0 1 .4 1 1 0 1.3.2 2.5.6 3.6.1.3 0 .7-.2 1z"/></svg>
          <span>970-555-0148</span>
        </li>
        <li>
          <svg viewBox="0 0 24 24" aria-hidden="true"><path fill="#4b7f9c" d="M2 5h20v14H2z"/><path fill="none" stroke="#fff" stroke-width="1.6" d="M2.5 5.5 12 13l9.5-7.5"/></svg>
          <span>dale@BrightHarvestHope.org</span>
        </li>
        <li>
          <svg viewBox="0 0 24 24" aria-hidden="true"><g fill="none" stroke="#4b7f9c" stroke-width="1.8"><circle cx="12" cy="12" r="9.5"/><ellipse cx="12" cy="12" rx="4.2" ry="9.5"/><path d="M2.5 12h19M4 7h16M4 17h16"/></g></svg>
          <span>www.BrightHarvestHope.org</span>
        </li>
      </ul>
    </div>
  </section>
</main>
</body>
</html>
```